Business card design for web travel company

Hi
we'd like to receive some proposal for a business card design.
Stayvano is a private travel club, dedicated to all travel lovers, with unique offers for exclusive destinations all around the world. At Stayvano you can find a wide range of offers for resorts, boutique hotels and travel packages at the best guaranteed price available on the market. The convenience of the offer is guaranteed by a private sales model: offers are available for a limited time only and they are personally chosen by Stayvano's qualified team of travel experts.
We offer only exclusive hotels with discounted prices but we are not an outlet or a discount supermarket: the design should reflect our connection with luxury, exclusivity using the same style of our website www.stayvano-example.com.
We want to make sure that when we'll present ourself to our business partner they will feel immediately which is our brand positioning giving them also a sense of an affordable and reliable partner.
In attachment you can also find our brand guidelines (please note that we are NOT USING ANY MORE THE TAG LINE "Five star outlet" mentioned in it).
The info to be inserted are:
Name Surname
Job Title
Tel
Mobile (when needed)
Email
Stayvano S.r.l.
Via Bruno Lesta 27
20131 Milano

```html
<!DOCTYPE html>
<html lang="en">
<head>
<meta charset="utf-8">
<title>Stayvano business card</title>
<link rel="stylesheet" href="https://fonts.googleapis.com/css2?family=Open+Sans:wght@300;400;600&display=swap">
<style>
  :root {
    --backdrop: #3a2a2c;
    --card: #050505;
    --card-texture: #101010;
    --white: #ffffff;
    --gold: #d6c68c;
    --muted: #d9d9d9;
  }
  html, body {
    margin: 0;
    padding: 0;
    width: 1200px;
    height: 1024px;
    overflow: hidden;
    background: var(--backdrop);
    font-family: "Open Sans", sans-serif;
  }
  .canvas {
    position: relative;
    width: 1200px;
    height: 1024px;
  }
  .card {
    position: absolute;
    width: 434px;
    height: 248px;
    background: var(--card);
    color: var(--white);
    box-shadow: 0 2px 6px rgba(0,0,0,0.35);
  }
  .card--front { left: 120px; top: 263px; }
  .card--back { left: 586px; top: 265px; }
  .card--details { left: 508px; top: 552px; }
  .texture {
    position: absolute;
    inset: 0;
    background: var(--card-texture);
  }
  .abs { position: absolute; white-space: nowrap; line-height: 1; }

  .front-name {
    left: 0; width: 100%; top: 110px;
    text-align: center;
    font-size: 32px;
    font-weight: 300;
    letter-spacing: 0.5px;
  }
  .front-url {
    left: 0; width: 100%; top: 150px;
    text-align: center;
    font-size: 13px;
    font-weight: 300;
    letter-spacing: 3.2px;
  }
  .back-url {
    right: 21px; top: 206px;
    font-size: 14px;
    font-weight: 400;
  }

  .person-name {
    right: 251px; top: 50px;
    font-size: 16px;
    font-weight: 600;
    color: var(--gold);
  }
  .person-role {
    right: 251px; top: 71px;
    font-size: 12.5px;
    font-weight: 300;
    color: var(--muted);
    letter-spacing: 0.5px;
  }
  .divider {
    left: 203px; top: 48px;
    width: 2px; height: 178px;
    background: var(--white);
  }
  .details-name {
    left: 233px; top: 84px;
    font-size: 26px;
    font-weight: 300;
  }
  .address {
    left: 233px; top: 128px;
    font-size: 10.5px;
    font-weight: 300;
    line-height: 14.6px;
    color: var(--muted);
  }
  .contacts {
    left: 233px; top: 180px;
    margin: 0; padding: 0;
    list-style: none;
    font-size: 10.5px;
    font-weight: 300;
    color: var(--muted);
  }
  .contacts li {
    display: flex;
    align-items: center;
    height: 15.7px;
  }
  .contacts svg {
    width: 12px; height: 10px;
    margin-right: 10px;
    flex: none;
  }
</style>
</head>
<body>
<main class="canvas">

  <section class="card card--front" aria-label="Card front">
    <div class="texture" role="img" aria-label="Fine diagonal pinstripe texture"></div>
    <div class="abs front-name">Stayvano</div>
    <div class="abs front-url">www.stayvano-example.com</div>
  </section>

  <section class="card card--back" aria-label="Card back">
    <div class="texture" role="img" aria-label="Fine diagonal pinstripe texture"></div>
    <div class="abs back-url">www.stayvano-example.com</div>
  </section>

  <section class="card card--details" aria-label="Card details side">
    <div class="abs person-name">Marco Vellani</div>
    <div class="abs person-role">Marketing Manager</div>
    <div class="abs divider"></div>
    <div class="abs details-name">Stayvano</div>
    <address class="abs address" style="font-style:normal">
      Stayvano S.r.l.<br>
      Via Bruno Lesta 27<br>
      20131 Milano
    </address>
    <ul class="abs contacts">
      <li>
        <svg viewBox="0 0 12 10" aria-hidden="true">
          <path d="M1 4 Q6 0 11 4 L10 5.5 L8 4.5 L8 3.5 Q6 2.8 4 3.5 L4 4.5 L2 5.5 Z" fill="var(--gold)"/>
          <rect x="3" y="5" width="6" height="4" rx="1" fill="var(--gold)"/>
        </svg>
        02 555 0143
      </li>
      <li>
        <svg viewBox="0 0 12 10" aria-hidden="true">
          <rect x="1" y="7" width="1.8" height="3" fill="var(--gold)"/>
          <rect x="3.8" y="5" width="1.8" height="5" fill="var(--gold)"/>
          <rect x="6.6" y="3" width="1.8" height="7" fill="var(--gold)"/>
          <rect x="9.4" y="1" width="1.8" height="9" fill="var(--gold)"/>
        </svg>
        02 555 0143
      </li>
      <li>
        <svg viewBox="0 0 12 10" aria-hidden="true">
          <rect x="1" y="2" width="10" height="7" fill="none" stroke="var(--gold)" stroke-width="1"/>
          <path d="M1 2 L6 6 L11 2" fill="none" stroke="var(--gold)" stroke-width="1"/>
        </svg>
        info@stayvano-example.com
      </li>
    </ul>
  </section>

</main>
</body>
</html>
```